Brackenford Group Website

We have a newly established brand for a company with an existing portfolio of property. The company is corporate and professional and both owns and develops property. The website should reflect a professional and stable organisation. The website should showcase the existing properties (6), have a home page that describes the company and its activities and has a "about us" page. The website will be in Wordpress and we would like the code for all pages to be sent to us by the successful designer upon completion of the job.
Updates

sorry was called from the office on an urgent matter. To be fair on submitters, i need a couple more days to finalise reviews.

Contact Information for Business Card

Brackenford Logo on front
Black background with silver logo.

Coding

Number of Pages Required

Colors

Designer to choose colors to be used in the design.

Requirements
Must have
• Text side of card should include
• Brackenford Property Group (as title in logo font)
• Employee Name (centered)
• Job Title (centered below name)
• Address 4 lines
• Email, mobile office phone, 3 lines
• website address (probably as footer)

```html
<!DOCTYPE html>
<html lang="en">
<head>
<meta charset="utf-8">
<title>Ashmere Case Study – Brackenford Group</title>
<link href="https://fonts.googleapis.com/css2?family=Mulish:wght@400;600;700;800&display=swap" rel="stylesheet">
<style>
:root{
  --ink:#1f1f1f;
  --text:#555;
  --muted:#8a8a8a;
  --dark:#141414;
  --dark-2:#1c1c1c;
  --page:#eeeeee;
  --card:#ffffff;
  --line:#dcdcdc;
  --silver:#c9c9c9;
  --icon-bg:#333;
  --white:#ffffff;
}
*{box-sizing:border-box;margin:0;padding:0}
html,body{width:1200px;height:2428px;overflow:hidden}
body{background:var(--page);font-family:"Mulish",Arial,sans-serif;color:var(--text);position:relative}

/* header */
.site-header{position:absolute;left:0;top:0;width:1200px;height:188px;background:var(--dark)}
.brand{position:absolute;left:120px;top:66px;display:flex;align-items:center;gap:14px}
.brand-mark{width:34px;height:34px;border:2px solid var(--silver);border-radius:50%}
.brand-name{font-size:28px;font-weight:700;color:var(--silver)}
.utility{position:absolute;right:120px;top:26px;display:flex;gap:36px;font-size:13px;letter-spacing:1.5px;color:var(--silver);text-transform:uppercase}
.utility span{display:flex;align-items:center;gap:8px}
.main-nav{position:absolute;right:120px;top:84px;display:flex;gap:38px;font-size:15px;font-weight:700;letter-spacing:1.5px;color:var(--white);text-transform:uppercase}
.main-nav .active{border-bottom:2px solid var(--white);padding-bottom:6px}

/* page heading */
.breadcrumb{position:absolute;left:120px;top:268px;font-size:14px;font-weight:700;letter-spacing:2px;color:var(--ink);text-transform:uppercase;display:flex;align-items:center;gap:12px}
.breadcrumb::before{content:"";width:36px;height:2px;background:var(--ink)}
.page-title{position:absolute;left:120px;top:306px;font-size:30px;font-weight:800;color:var(--ink);letter-spacing:.5px;text-transform:uppercase}

/* card */
.case-card{position:absolute;left:120px;top:372px;width:960px;height:1748px;background:var(--card);padding:20px 32px 0 40px;display:flex;gap:36px}
.gallery{width:400px;display:flex;flex-direction:column;gap:12px}
.photo{width:400px}
.photo-1{height:360px;background:linear-gradient(160deg,#dfe4e8,#b8bdc0 55%,#8f9497)}
.photo-2{height:310px;background:linear-gradient(180deg,#e8e6e2,#c9c4bc 60%,#a59e94)}
.photo-3{height:300px;background:linear-gradient(170deg,#d7dde2,#b1b7bb 50%,#7c8184)}
.photo-4{height:330px;background:linear-gradient(180deg,#eef0f2,#c6c9cb 55%,#8e9193)}
.photo-5{height:340px;background:linear-gradient(180deg,#1c2a4a,#34467a 45%,#6a5a7c 75%,#2a2438)}

.details{flex:1;padding-top:10px}
.details h2{font-size:21px;font-weight:800;color:var(--ink);letter-spacing:1px;text-transform:uppercase;margin-bottom:14px}
.details p{font-size:14.5px;line-height:1.65;margin-bottom:14px}
.section{margin-bottom:34px}
.section-result{margin-top:150px}

.facts{display:flex;gap:44px;margin-top:4px}
.fact strong{display:block;font-size:56px;font-weight:700;color:var(--ink);line-height:1}
.fact span{display:block;font-size:14px;line-height:1.4;margin-top:8px;width:120px}

.address-list{list-style:none;font-size:14.5px;line-height:1.6}
.address-list li{display:flex;gap:14px;padding:10px 0;border-bottom:1px solid var(--line)}
.address-list li:last-child{border-bottom:0}
.address-list svg{flex:none;margin-top:3px}

.units{width:100%;border-collapse:collapse;font-size:14.5px}
.units td{padding:7px 0;border-bottom:1px solid var(--line)}
.units td:first-child{width:46%}

/* footer */
.site-footer{position:absolute;left:0;top:2150px;width:1200px;height:278px;background:var(--dark-2);color:var(--silver)}
.footer-brand{position:absolute;left:0;width:1200px;top:28px;display:flex;justify-content:center;align-items:center;gap:12px}
.footer-brand .brand-mark{width:28px;height:28px}
.footer-brand .brand-name{font-size:22px}
.footer-contacts{position:absolute;left:120px;top:92px;width:960px;display:flex;justify-content:space-between}
.contact{width:210px;text-align:center;font-size:13px;line-height:1.5;color:var(--silver)}
.contact-icon{width:34px;height:34px;border-radius:50%;background:var(--icon-bg);display:flex;align-items:center;justify-content:center;margin:0 auto 8px}
.social{position:absolute;left:0;width:1200px;top:222px;display:flex;justify-content:center;gap:18px}
.social a{width:24px;height:24px;display:flex;align-items:center;justify-content:center}
.copyright{position:absolute;left:0;width:1200px;top:256px;text-align:center;font-size:11px;color:var(--muted)}
</style>
</head>
<body>

<header class="site-header">
  <div class="brand">
    <span class="brand-mark"></span>
    <span class="brand-name">Brackenford</span>
  </div>
  <div class="utility">
    <span><svg width="12" height="12" viewBox="0 0 12 12"><circle cx="5" cy="5" r="4" fill="none" stroke="#c9c9c9" stroke-width="1.5"/><line x1="8" y1="8" x2="11" y2="11" stroke="#c9c9c9" stroke-width="1.5"/></svg>Search</span>
    <span><svg width="12" height="12" viewBox="0 0 12 12"><circle cx="6" cy="4" r="3" fill="#c9c9c9"/><path d="M1 12a5 5 0 0 1 10 0z" fill="#c9c9c9"/></svg>Investor Login</span>
  </div>
  <nav class="main-nav">
    <span>About</span><span>Expertise</span><span class="active">Case Studies</span><span>Team</span><span>Contact Us</span>
  </nav>
</header>

<div class="breadcrumb">Case Studies</div>
<h1 class="page-title">Ashmere, 41 Kestrel Av, Auckland CBD</h1>

<main class="case-card">
  <div class="gallery">
    <div class="photo photo-1" role="img" aria-label="Exterior of the finished apartment building on a corner site"></div>
    <div class="photo photo-2" role="img" aria-label="Open-plan apartment interior with living area"></div>
    <div class="photo photo-3" role="img" aria-label="Street view of the building facade and balconies"></div>
    <div class="photo photo-4" role="img" aria-label="Modern kitchen and dining space inside an apartment"></div>
    <div class="photo photo-5" role="img" aria-label="City skyline at dusk with the tower lit up"></div>
  </div>

  <div class="details">
    <section class="section">
      <h2>The Vision</h2>
      <p>The building was a run-down mid-century block with a low earthquake rating. In this central part of Auckland we saw the chance for a fresh boutique apartment building.</p>
    </section>

    <section class="section">
      <h2>The Project</h2>
      <p>We added an extra floor to the building, and while restoring the front and rear walls, fully removed the internal partitions and walls. We strengthened the walls and parapets and rebuilt the foundations. New lifts were installed and all walls were plastered and painted. Internally we laid quality carpet and specialty flooring throughout, upgraded the ground floor retail, exposed services and conditioned the common walls back to bare brick.</p>
      <p>We then laid out a modern series of apartments over five floors with a central corridor. We improved the ceilings and services, installed quality fittings and specialty tapware and created a new first floor deck area.</p>
      <p>We fully fitted out all apartments with quality furnished fabrics and soft goods.</p>
      <p>The units were then let to numerous corporate clients on short and long term leases. Clients included national firms whose staff enjoyed comfort and security in a boutique building with high levels of security.</p>
      <p>We carefully selected a complementary retailer for the ground floor tenancy whose urban fitout aesthetic now draws crowds.</p>
    </section>

    <section class="section section-result">
      <h2>The Result</h2>
      <p>The newly finished Ashmere apartment building provided a high yield and significant value uplift and qualifies as an institutional quality asset.</p>
    </section>

    <section class="section">
      <h2>Key Facts</h2>
      <div class="facts">
        <div class="fact"><strong>215</strong><span>Total apartments let to date</span></div>
        <div class="fact"><strong>184</strong><span>Long term leases signed</span></div>
        <div class="fact"><strong>25</strong><span>Corporate clients housed</span></div>
      </div>
    </section>

    <section class="section">
      <h2>Address</h2>
      <ul class="address-list">
        <li><svg width="12" height="16" viewBox="0 0 12 16"><path d="M6 0a6 6 0 0 0-6 6c0 4.5 6 10 6 10s6-5.5 6-10a6 6 0 0 0-6-6z" fill="#555"/><circle cx="6" cy="6" r="2.2" fill="#fff"/></svg>Brackenford Group Ltd Level 8, Harrow House 10 Harrow Lane Auckland CBD</li>
        <li><svg width="14" height="14" viewBox="0 0 14 14"><path d="M3 0l3 3-2 2a9 9 0 0 0 5 5l2-2 3 3-2 3C6 14 0 8 0 3z" fill="#555"/></svg>Phone: &nbsp;+64 9 555 0142</li>
        <li><svg width="14" height="12" viewBox="0 0 14 12"><rect x="0.5" y="0.5" width="13" height="11" fill="none" stroke="#555"/><path d="M0.5 0.5l6.5 6 6.5-6" fill="none" stroke="#555"/></svg>Email: &nbsp;team@brackenfordgroup.co.nz</li>
      </ul>
    </section>

    <section class="section">
      <h2>Units</h2>
      <table class="units">
        <tr><td>Retail</td><td>150 m²</td></tr>
        <tr><td>Apartments</td><td>89</td></tr>
        <tr><td>Total Floor Area</td><td>2200 m²</td></tr>
        <tr><td>Basement</td><td>Parking and storage</td></tr>
        <tr><td>Date Completed</td><td>April 2016</td></tr>
        <tr><td>Completed value</td><td>$25.6m</td></tr>
      </table>
    </section>
  </div>
</main>

<footer class="site-footer">
  <div class="footer-brand">
    <span class="brand-mark"></span>
    <span class="brand-name">Brackenford</span>
  </div>
  <div class="footer-contacts">
    <div class="contact">
      <div class="contact-icon"><svg width="12" height="16" viewBox="0 0 12 16"><path d="M6 0a6 6 0 0 0-6 6c0 4.5 6 10 6 10s6-5.5 6-10a6 6 0 0 0-6-6z" fill="#c9c9c9"/><circle cx="6" cy="6" r="2.2" fill="#333"/></svg></div>
      Brackenford Group Ltd<br>Level 8, Harrow House<br>10 Harrow Lane<br>Auckland CBD
    </div>
    <div class="contact">
      <div class="contact-icon"><svg width="14" height="12" viewBox="0 0 14 12"><rect x="0.5" y="0.5" width="13" height="11" fill="none" stroke="#c9c9c9"/><path d="M0.5 0.5l6.5 6 6.5-6" fill="none" stroke="#c9c9c9"/></svg></div>
      PO Box 4021<br>Harbour St Auckland 1140
    </div>
    <div class="contact">
      <div class="contact-icon"><svg width="14" height="14" viewBox="0 0 14 14"><path d="M3 0l3 3-2 2a9 9 0 0 0 5 5l2-2 3 3-2 3C6 14 0 8 0 3z" fill="#c9c9c9"/></svg></div>
      Phone:<br>+64 9 555 0142
    </div>
    <div class="contact">
      <div class="contact-icon"><svg width="14" height="12" viewBox="0 0 14 12"><rect x="0.5" y="0.5" width="13" height="11" fill="none" stroke="#c9c9c9"/><path d="M0.5 0.5l6.5 6 6.5-6" fill="none" stroke="#c9c9c9"/></svg></div>
      Email:<br>team@brackenfordgroup.co.nz
    </div>
  </div>
  <div class="social" aria-label="Share links">
    <a aria-label="Share"><svg width="16" height="16" viewBox="0 0 16 16"><circle cx="12" cy="3" r="2.2" fill="#c9c9c9"/><circle cx="4" cy="8" r="2.2" fill="#c9c9c9"/><circle cx="12" cy="13" r="2.2" fill="#c9c9c9"/><path d="M12 3L4 8l8 5" fill="none" stroke="#c9c9c9" stroke-width="1.4"/></svg></a>
    <a aria-label="Message"><svg width="16" height="16" viewBox="0 0 16 16"><path d="M2 2h12v9H6l-4 3z" fill="none" stroke="#c9c9c9" stroke-width="1.6" stroke-linejoin="round"/></svg></a>
    <a aria-label="Link"><svg width="16" height="16" viewBox="0 0 16 16"><rect x="1" y="5.5" width="8" height="5" rx="2.5" fill="none" stroke="#c9c9c9" stroke-width="1.6"/><rect x="7" y="5.5" width="8" height="5" rx="2.5" fill="none" stroke="#c9c9c9" stroke-width="1.6"/></svg></a>
    <a aria-label="Website"><svg width="16" height="16" viewBox="0 0 16 16"><circle cx="8" cy="8" r="6.5" fill="none" stroke="#c9c9c9" stroke-width="1.4"/><ellipse cx="8" cy="8" rx="3" ry="6.5" fill="none" stroke="#c9c9c9" stroke-width="1.2"/><line x1="1.5" y1="8" x2="14.5" y2="8" stroke="#c9c9c9" stroke-width="1.2"/></svg></a>
  </div>
  <div class="copyright">© 2016 Brackenford Property Group, all rights reserved.</div>
</footer>

</body>
</html>
```